Business card and stationary for consulting business

We need business cards and matching stationary for professional consulting business for employment and human resources issues.
One of the CraftHive designers designed the logo with our company name.  Use the colors in the logo and may use light yellow as an accent color.
Add
Mara T. Vollen, J.D., LL.M.
485 E. Callister Lane
Winter Park, Florida  32789
407-555-0183
maravollenjd@quillpost.example

Industry/Entity Type
Business

```html
<!DOCTYPE html>
<html lang="en">
<head>
<meta charset="utf-8">
<title>Mara T. Vollen — Business Card</title>
<link rel="stylesheet" href="https://fonts.googleapis.com/css2?family=PT+Sans:wght@700&family=PT+Sans+Narrow:wght@400;700&display=swap">
<style>
  :root {
    --card-black: #0d0d0d;
    --card-charcoal: #1c1c1c;
    --accent-yellow: #f4ee52;
    --fold-white: #ffffff;
    --brand-cyan: #00b1e1;
    --brand-navy: #2d4689;
    --credential-navy: #264c8e;
    --name-white: #ffffff;
  }
  html, body {
    margin: 0;
    padding: 0;
    width: 1200px;
    height: 771px;
    overflow: hidden;
    background: var(--card-black);
  }
  .card {
    position: relative;
    width: 1200px;
    height: 771px;
    overflow: hidden;
    background:
      radial-gradient(ellipse at 50% 35%, var(--card-charcoal) 0%, var(--card-black) 75%);
  }
  .accent-stripe {
    position: absolute;
    left: 0;
    top: 0;
    width: 144px;
    height: 771px;
    background: var(--accent-yellow);
  }
  .corner-fold {
    position: absolute;
    left: 0;
    top: 0;
    width: 76px;
    height: 80px;
  }
  .name-plate {
    position: absolute;
    left: 144px;
    top: 279px;
    width: 603px;
    height: 211px;
    display: flex;
    box-shadow: 4px 8px 10px rgba(0, 0, 0, 0.75);
  }
  .name-block {
    width: 503px;
    background: var(--brand-cyan);
    position: relative;
  }
  .holder-name {
    position: absolute;
    right: 26px;
    top: 18px;
    margin: 0;
    font-family: "PT Sans", sans-serif;
    font-weight: 700;
    font-size: 70px;
    letter-spacing: -2.5px;
    color: var(--name-white);
    white-space: nowrap;
  }
  .holder-credentials {
    position: absolute;
    right: 26px;
    top: 114px;
    margin: 0;
    font-family: "PT Sans Narrow", sans-serif;
    font-weight: 400;
    font-size: 60px;
    letter-spacing: -2px;
    color: var(--credential-navy);
    white-space: nowrap;
  }
  .icon-column {
    width: 100px;
    background: var(--brand-navy);
    display: flex;
    flex-direction: column;
    align-items: center;
    justify-content: space-around;
    padding: 12px 0;
    box-sizing: border-box;
  }
  .icon { display: block; }
  .contact-line {
    position: absolute;
    left: 774px;
    margin: 0;
    font-family: "PT Sans Narrow", sans-serif;
    font-weight: 400;
    color: var(--brand-cyan);
    white-space: nowrap;
    letter-spacing: -0.5px;
  }
  .contact-phone { top: 308px; font-size: 46px; }
  .contact-email { top: 426px; font-size: 36px; }
</style>
</head>
<body>
<main class="card">
  <div class="accent-stripe"></div>
  <svg class="corner-fold" viewBox="0 0 76 80" aria-hidden="true">
    <defs>
      <filter id="fold-shadow" x="-20%" y="-20%" width="160%" height="160%">
        <feDropShadow dx="3" dy="4" stdDeviation="3" flood-color="#000" flood-opacity="0.7"/>
      </filter>
    </defs>
    <polygon points="0,0 66,0 0,72" fill="var(--fold-white)"/>
    <polygon points="66,0 66,72 0,72" fill="var(--accent-yellow)" filter="url(#fold-shadow)"/>
  </svg>

  <section class="name-plate">
    <div class="name-block">
      <h1 class="holder-name">Mara T. Vollen</h1>
      <p class="holder-credentials">J.D., LL.M.</p>
    </div>
    <div class="icon-column">
      <svg class="icon icon-phone" width="76" height="64" viewBox="0 0 76 64" aria-label="Phone">
        <path d="M4 20 C4 6 72 6 72 20 L72 28 L56 28 L56 20 C46 16 30 16 20 20 L20 28 L4 28 Z" fill="var(--brand-cyan)"/>
        <path d="M20 26 L28 24 L48 24 L56 26 L66 60 L10 60 Z" fill="var(--brand-cyan)"/>
        <circle cx="38" cy="44" r="8" fill="var(--brand-navy)"/>
      </svg>
      <svg class="icon icon-mail" width="76" height="56" viewBox="0 0 76 56" aria-label="Email">
        <rect x="2" y="2" width="72" height="52" fill="none" stroke="var(--brand-cyan)" stroke-width="4"/>
        <polyline points="2,2 38,32 74,2" fill="none" stroke="var(--brand-cyan)" stroke-width="4"/>
        <line x1="2" y1="54" x2="30" y2="26" stroke="var(--brand-cyan)" stroke-width="4"/>
        <line x1="74" y1="54" x2="46" y2="26" stroke="var(--brand-cyan)" stroke-width="4"/>
      </svg>
    </div>
  </section>

  <p class="contact-line contact-phone">407-555-0183</p>
  <p class="contact-line contact-email">maravollenjd@quillpost.example</p>
</main>
</body>
</html>
```